Letterhead for Conveyancing Company

Use existing logo to create a letterhead for a conveyancing company. Must be able to be used in Microsoft Word. Easy to read and professional.
Contact information to be at the bottom.
Brightwater Conveyancing Pty Ltd
ACN 621 984 736PO Box 535 Campbelltown SA 5074
Mobile - 0461 739 285
Web address - www.brightwaterconveyancing.com.au

Requirements
Must have
• Logo and contact details.
• Simple and professional.

```html
<!DOCTYPE html>
<html lang="en">
<head>
<meta charset="utf-8">
<title>Brightwater Conveyancing – Letterhead</title>
<link rel="stylesheet" href="https://fonts.googleapis.com/css2?family=Roboto:wght@400;500;700&family=Ubuntu:wght@500&family=Allura&display=swap">
<style>
  :root {
    --backdrop: #808080;
    --paper: #fafafa;
    --ink: #5c5c5c;
    --ink-strong: #4a4a4a;
    --brand: #e0449a;
    --rule: #8a8a8a;
    --ghost: #efefef;
    --signature: #2f4a7a;
  }
  * { box-sizing: border-box; margin: 0; padding: 0; }
  html, body { width: 1062px; height: 1200px; overflow: hidden; }
  body {
    background: var(--backdrop);
    font-family: "Roboto", Arial, sans-serif;
    color: var(--ink);
    position: relative;
  }
  .letterhead {
    position: absolute;
    left: 200px; top: 132px;
    width: 661px; height: 936px;
    background: var(--paper);
  }
  .brand-name {
    position: absolute;
    left: 41px; top: 52px;
    width: 170px;
    font-weight: 700;
    font-size: 30px;
    line-height: 32px;
    color: var(--brand);
  }
  .brand-ghost {
    position: absolute;
    left: 89px; top: 305px;
    font-weight: 700;
    font-size: 84px;
    line-height: 1;
    color: var(--ghost);
    white-space: nowrap;
  }
  .letter-body {
    position: absolute;
    left: 41px; top: 0;
    width: 578px;
    font-size: 11.2px;
    line-height: 15px;
  }
  .letter-date { position: absolute; top: 207px; }
  .recipient { position: absolute; top: 252px; font-style: normal; }
  .recipient-name { font-weight: 700; color: var(--ink-strong); }
  .salutation { position: absolute; top: 342px; }
  .letter-text { position: absolute; top: 373px; width: 578px; }
  .letter-text p { text-align: justify; margin-bottom: 15px; }
  .sign-off { position: absolute; top: 718px; }
  .signer-name { font-weight: 700; color: var(--ink-strong); }
  .signature {
    font-family: "Allura", cursive;
    font-size: 30px;
    line-height: 40px;
    color: var(--signature);
    margin: 2px 0 2px -12px;
  }
  .signer-role { margin-top: 2px; }
  .footer {
    position: absolute;
    left: 33px; top: 861px;
    width: 595px;
  }
  .footer-title {
    display: flex; align-items: center; gap: 10px;
    font-family: "Ubuntu", sans-serif;
    font-weight: 500;
    font-size: 15px;
    color: var(--brand);
    white-space: nowrap;
  }
  .footer-title::before, .footer-title::after {
    content: ""; flex: 1; height: 1.5px; background: var(--rule);
  }
  .contact-line {
    display: flex; justify-content: center; gap: 9px;
    margin-top: 8px;
    font-size: 11px;
    white-space: nowrap;
  }
  .contact-item { display: flex; align-items: center; gap: 4px; }
  .contact-item svg { width: 10px; height: 10px; fill: var(--brand); }
</style>
</head>
<body>
  <main class="letterhead">
    <div class="brand-name">Brightwater Conveyancing</div>
    <div class="brand-ghost" aria-hidden="true">Brightwater</div>

    <div class="letter-body">
      <p class="letter-date">30/20/2016</p>
      <address class="recipient">
        <div class="recipient-name">Mr. ABC Harlow</div>
        <div>123, Street No. 123,</div>
        <div>City Name</div>
        <div>Pincode-123456</div>
      </address>
      <p class="salutation">Dear Sir,</p>
      <div class="letter-text">
        <p>Lorem Ipsum is simply dummy text of the printing and typesetting industry. Lorem Ipsum has been the industry's standard dummy text ever since the 1500s, when an unknown printer took a galley of type and scrambled it to make a type specimen book. It has survived not only five centuries, but also the leap into electronic typesetting, remaining essentially unchanged. It was popularised in the 1960s with the release of Veltrace sheets containing Lorem Ipsum passages, and more recently with desktop publishing software like Orlin PageCraft including versions of Lorem Ipsum.</p>
        <p>Lorem Ipsum is simply dummy text of the printing and typesetting industry. Lorem Ipsum has been the industry's standard dummy text ever since the 1500s, when an unknown printer took a galley of type and scrambled it to make a type specimen book. It has survived not only five centuries, but also the leap into electronic typesetting, remaining essentially unchanged. It was popularised in the 1960s with the release of Veltrace sheets containing Lorem Ipsum passages, and more recently with desktop publishing software like Orlin PageCraft including versions of Lorem Ipsum.</p>
        <p>Lorem Ipsum is simply dummy text of the printing and typesetting industry. Lorem Ipsum has been the industry's standard dummy text ever since the 1500s, when an unknown printer took a galley of type and scrambled it to make a type specimen book.</p>
        <p>Lorem Ipsum is simply dummy text of the printing and typesetting industry. Lorem Ipsum has been the industry's standard dummy text ever since the 1500s, when an unknown printer took a galley of type and scrambled it to make a type specimen book.</p>
      </div>
      <div class="sign-off">
        <div class="signer-name">Your Name</div>
        <div class="signature">Your Signature</div>
        <div class="signer-role">CEO &nbsp;|&nbsp; Owner</div>
      </div>
    </div>

    <footer class="footer">
      <div class="footer-title">Brightwater Conveyancing Pty Ltd</div>
      <div class="contact-line">
        <span class="contact-item">
          <svg viewBox="0 0 10 10"><path d="M1 3.5C1 2 2.5 1.5 5 1.5S9 2 9 3.5v.8H7V3.3H3v1H1zM2 5h6l1 3.5H1z"/></svg>
          0461 739 285
        </span>
        <span class="contact-item">
          <svg viewBox="0 0 10 10"><path d="M5 .5a4.5 4.5 0 1 0 0 9 4.5 4.5 0 0 0 0-9zm0 1.2c.6.6 1 1.6 1.1 2.7H3.9C4 3.3 4.4 2.3 5 1.7zM1.7 5.6h1.1c.1.9.3 1.7.7 2.3A3.3 3.3 0 0 1 1.7 5.6zm0-1.2A3.3 3.3 0 0 1 3.5 2c-.4.7-.6 1.5-.7 2.4zm3.3 3.9c-.6-.6-1-1.6-1.1-2.7h2.2C6 6.7 5.6 7.7 5 8.3zm1.5-.4c.4-.6.6-1.4.7-2.3h1.1a3.3 3.3 0 0 1-1.8 2.3zm.7-3.5C7.1 3.5 6.9 2.7 6.5 2a3.3 3.3 0 0 1 1.8 2.4z"/></svg>
          www.brightwaterconveyancing.com.au
        </span>
        <span class="contact-item">
          <svg viewBox="0 0 10 10"><path d="M5 .5A3.2 3.2 0 0 0 1.8 3.7C1.8 6.2 5 9.5 5 9.5s3.2-3.3 3.2-5.8A3.2 3.2 0 0 0 5 .5zm0 4.5a1.3 1.3 0 1 1 0-2.6A1.3 1.3 0 0 1 5 5z"/></svg>
          PO Box 812 Glenhaven SA 5091
        </span>
        <span class="contact-item">
          <svg viewBox="0 0 10 10"><path d="M3 .5h1.3l-.3 2h2l.3-2h1.3l-.3 2h2v1.3h-2.2l-.3 2.4h2v1.3h-2.2l-.3 2H5l.3-2h-2l-.3 2H1.7l.3-2H0V6.2h2.2l.3-2.4H.5V2.5h2.2zm.8 3.3-.3 2.4h2l.3-2.4z"/></svg>
          ACN 738 215 409
        </span>
      </div>
    </footer>
  </main>
</body>
</html>
```